Keynote Presentation Design Project for Crazy technology innovation company

q7ventureworks is a company that do angel investments and consult/guide technology startups. In addition i have crazy innovation projects building hardware and software for fun (like tinkerloft.example). This is not a mainstream company, but has to be serious as well as innovative. Please also look at the website design here: http://q7ventureworks.com

Please look at these projects for description for my logo design and website design for more information about the company.

website: (completed)
http://jobs.briefhive.example/job.aspx?Id=61824

logo: (completed)
http://jobs.briefhive.example/job.aspx?Id=37590

Target Market(s)

entrepreneurs & investors

Industry/Entity Type

Building

Requirements
Must have
• page designs:
All default keynote master slides should be styled.

page component designs/colour palettes:
tables
charts (up to 4 colors/rows)
process (a few boxes, arrows etc)

Delivery must be a keynote file and color codes in hex for all colors, and fonts must either be delivered or named.

```html
<!DOCTYPE html>
<html lang="en">
<head>
<meta charset="utf-8">
<title>Q7 Ventureworks – Keynote Master Slides</title>
<link rel="stylesheet" href="https://fonts.googleapis.com/css2?family=Amatic+SC:wght@700&family=Arvo:wght@400&display=swap">
<style>
  :root {
    --page-bg: #eef0f2;
    --slide-center: #63acce;
    --slide-edge: #4a86a4;
    --text-light: #ffffff;
    --text-dark: #141414;
    --shape-top: #45b4e4;
    --shape-bottom: #1a88c4;
    --pie-2007: #8fdcfc;
    --pie-2008: #3eaedc;
    --pie-2009: #1a93d2;
    --pie-2010: #0c78ae;
    --pie-2011: #0a5e92;
    --pie-2012: #074675;
    --title-font: "Amatic SC", cursive;
    --body-font: "Arvo", serif;
  }
  html, body {
    margin: 0;
    padding: 0;
    overflow: hidden;
  }
  body {
    width: 1200px;
    height: 1000px;
    background: var(--page-bg);
    position: relative;
    font-family: var(--body-font);
  }
  .slide {
    position: absolute;
    overflow: hidden;
    background: radial-gradient(ellipse at 45% 45%, var(--slide-center) 0%, var(--slide-edge) 85%);
    box-shadow: 0 6px 18px rgba(0, 0, 0, 0.28);
  }
  .slide-texture {
    position: absolute;
    inset: 0;
    background: linear-gradient(160deg, rgba(255,255,255,0.06), rgba(255,255,255,0) 60%);
  }
  .slide-title {
    position: absolute;
    margin: 0;
    font-family: var(--title-font);
    font-weight: 700;
    color: var(--text-light);
    letter-spacing: 1px;
    line-height: 1;
    text-shadow: 0 2px 4px rgba(0,0,0,0.25);
  }
  .brand-name {
    position: absolute;
    margin: 0;
    font-family: var(--body-font);
    font-weight: 400;
    color: var(--text-light);
    line-height: 1;
    white-space: nowrap;
  }

  /* Slide 1: title and bullets */
  .slide-bullets { left: 110px; top: 40px; width: 940px; height: 520px; z-index: 1; }
  .slide-bullets .slide-title { left: 115px; top: 50px; font-size: 68px; }
  .slide-bullets .brand-name { right: 45px; top: 78px; font-size: 24px; }
  .bullet-list {
    position: absolute;
    left: 145px;
    top: 170px;
    margin: 0;
    padding: 0;
    list-style: disc;
    color: var(--text-dark);
    font-size: 25px;
  }
  .bullet-list li { margin-bottom: 28px; padding-left: 6px; }
  .bullet-list .inset { margin-left: 18px; }

  /* Slide 2: callouts and shapes */
  .slide-shapes { left: 530px; top: 300px; width: 640px; height: 400px; z-index: 2; }
  .slide-shapes .slide-title { left: 100px; top: 40px; font-size: 50px; }
  .slide-shapes .brand-name { right: 30px; top: 120px; font-size: 17px; }
  .shapes-art { position: absolute; left: 0; top: 0; }
  .shape-label { font-family: var(--body-font); font-size: 12px; fill: var(--text-light); }

  /* Slide 3: chart */
  .slide-chart { left: 50px; top: 570px; width: 660px; height: 375px; z-index: 3; }
  .slide-chart .brand-name { right: 55px; top: 36px; font-size: 17px; }
  .chart-art { position: absolute; left: 0; top: 0; }
  .pie-label { font-family: var(--body-font); font-size: 11px; fill: var(--text-light); }
  .legend-label { font-family: var(--body-font); font-size: 11px; fill: var(--text-light); }
</style>
</head>
<body>

<section class="slide slide-bullets">
  <div class="slide-texture" role="img" aria-label="Soft hand-drawn grid texture behind the slide"></div>
  <h1 class="slide-title">Title and Bullets Slide</h1>
  <p class="brand-name">Q7 Ventureworks</p>
  <ul class="bullet-list">
    <li>Bullet item 1</li>
    <li class="inset">Inset bullet item 1</li>
    <li class="inset">Inset bullet item 2</li>
    <li>Bullet item 2</li>
  </ul>
</section>

<section class="slide slide-shapes">
  <div class="slide-texture" role="img" aria-label="Soft hand-drawn grid texture behind the slide"></div>
  <h2 class="slide-title">Callouts and Shapes</h2>
  <p class="brand-name">Q7 Ventureworks</p>
  <svg class="shapes-art" width="640" height="400" viewBox="0 0 640 400">
    <defs>
      <linearGradient id="shapeFill" x1="0" y1="0" x2="0" y2="1">
        <stop offset="0" stop-color="var(--shape-top)"/>
        <stop offset="1" stop-color="var(--shape-bottom)"/>
      </linearGradient>
    </defs>
    <g stroke="#ffffff" stroke-width="1.5" fill="url(#shapeFill)">
      <rect class="shape-box" x="115" y="170" width="70" height="55"/>
      <rect class="shape-rounded" x="205" y="170" width="68" height="60" rx="6"/>
      <circle class="shape-oval" cx="320" cy="222" r="28"/>
      <path class="shape-callout" d="M375 212 h92 a5 5 0 0 1 5 5 v42 a5 5 0 0 1 -5 5 h-87 a5 5 0 0 1 -5 -5 v-30 l-10 -8 l10 -4 z"/>
      <path class="shape-quote" d="M508 232 a30 30 0 1 1 -8 40 l-10 5 l6 -12 a30 30 0 0 1 12 -33 z"/>
      <path class="arrow-single" d="M190 270 h100 v-10 l25 18 l-25 18 v-10 h-100 z"/>
      <path class="arrow-double" d="M328 288 l22 -18 v9 h78 v-9 l22 18 l-22 18 v-9 h-78 v9 z"/>
    </g>
    <g stroke="#ffffff" stroke-width="1.5" fill="none">
      <line x1="515" y1="320" x2="465" y2="316"/>
      <path d="M472 312 l-7 4 l7 5"/>
    </g>
    <text class="shape-label" x="150" y="201" text-anchor="middle">Box</text>
    <text class="shape-label" x="239" y="196" text-anchor="middle">Rounded</text>
    <text class="shape-label" x="239" y="212" text-anchor="middle">Box</text>
    <text class="shape-label" x="320" y="226" text-anchor="middle">Oval</text>
    <text class="shape-label" x="424" y="243" text-anchor="middle">Callout Box</text>
    <text class="shape-label" x="530" y="257" text-anchor="middle">Quote</text>
    <text class="shape-label" x="530" y="273" text-anchor="middle">Bubble</text>
    <text class="shape-label" x="240" y="282" text-anchor="middle">Single Arrow</text>
    <text class="shape-label" x="389" y="292" text-anchor="middle">Double Arrow</text>
  </svg>
</section>

<section class="slide slide-chart">
  <div class="slide-texture" role="img" aria-label="Soft hand-drawn grid texture behind the slide"></div>
  <p class="brand-name">Q7 Ventureworks</p>
  <svg class="chart-art" width="660" height="375" viewBox="0 0 660 375">
    <g class="legend" transform="translate(155 205)">
      <circle cx="0" cy="0" r="4.5" fill="var(--pie-2007)"/><text class="legend-label" x="12" y="4">2007</text>
      <circle cx="0" cy="17" r="4.5" fill="var(--pie-2008)"/><text class="legend-label" x="12" y="21">2008</text>
      <circle cx="0" cy="34" r="4.5" fill="var(--pie-2009)"/><text class="legend-label" x="12" y="38">2009</text>
      <circle cx="0" cy="51" r="4.5" fill="var(--pie-2010)"/><text class="legend-label" x="12" y="55">2010</text>
      <circle cx="0" cy="68" r="4.5" fill="var(--pie-2011)"/><text class="legend-label" x="12" y="72">2011</text>
      <circle cx="0" cy="85" r="4.5" fill="var(--pie-2012)"/><text class="legend-label" x="12" y="89">2012</text>
    </g>
    <g class="pie" transform="translate(328 232)" stroke="#4f8fae" stroke-width="1">
      <path d="M0 0 L0 -90 A90 90 0 0 1 72.81 52.90 Z" fill="var(--pie-2007)"/>
      <path d="M0 0 L72.81 52.90 A90 90 0 0 1 -69.35 57.37 Z" fill="var(--pie-2008)"/>
      <path d="M0 0 L-69.35 57.37 A90 90 0 0 1 -90 0 Z" fill="var(--pie-2009)"/>
      <path d="M0 0 L-90 0 A90 90 0 0 1 -72.81 -52.90 Z" fill="var(--pie-2010)"/>
      <path d="M0 0 L-72.81 -52.90 A90 90 0 0 1 -38.32 -81.43 Z" fill="var(--pie-2011)"/>
      <path d="M0 0 L-38.32 -81.43 A90 90 0 0 1 0 -90 Z" fill="var(--pie-2012)"/>
      <g stroke="none">
        <text class="pie-label" x="55" y="-24" text-anchor="middle">35%</text>
        <text class="pie-label" x="4" y="70" text-anchor="middle">29%</text>
        <text class="pie-label" x="-54" y="24" text-anchor="middle">11%</text>
        <text class="pie-label" x="-57" y="-15" text-anchor="middle">10%</text>
        <text class="pie-label" x="-40" y="-43" text-anchor="middle">8%</text>
        <text class="pie-label" x="-15" y="-57" text-anchor="middle">7%</text>
      </g>
    </g>
  </svg>
</section>

</body>
</html>
```